Seeking a beautiful packaging box for Dusk Haven - an essential oil blend (mock up provided!)

My sleep brand - Dusk Haven - is almost ready to go to market. And I need a box! Dusk Haven is a high end essential oils/sleep hygiene brand.

I need a gorgeous, classy box for our 3 sizes of essential oil product we are selling. I have a draft mockup which is to approximate size (attached), but need some help with the finishing touches and layout so it's really polished. I am looking for simple/monochrome designs using black and off white (think Norvel inspo!)

We are selling a 15mL dropper bottle and two roll ons (5ml, 10ml) of the essential oil blend. These are all amber bottles with black top. The box design will be almost identical for each, with very slight variations due to size differences.

The size of the boxes will be
15mL dropper: 30x30x95mm
10ml roller: 19x19x88mm
5ml roller: 18x18x59mm

Target Market(s)

High end/high price point product, shift workers, mums, people suffering stress and insomnia

Industry/Entity Type

Health And Wellness

Font styles to use
Serif
Sans Serif

Colors

Designer to choose only greyscale colors for use in the design.

Requirements
Must have
• I have attached a word document which includes all the necessary text:
- ingredients
- directions
- cautions
- info on essential oils/dusk haven (abbreviated on the smallest box)

Additionally:
- volume
- our website
- instagram logo/duskhavenau name
- made in australia
- recycle symbol
- 12 month open symbol
Nice to have
• I would like the boxes to be monochromatic: white or off white colour, with black logo and writing. I am open to variations on the logo (ie position of writing in relation to the circle/change of font size), but mostly need help with layout, font, direction of text, design of the blank spaces, patterns etc.
Should not have
• Colours

```html
<!DOCTYPE html>
<html lang="en">
<head>
<meta charset="utf-8">
<title>Dusk Haven – Essential Oil Blend Box Dieline</title>
<link rel="stylesheet" href="https://fonts.googleapis.com/css2?family=EB+Garamond:wght@400;600&family=Cormorant+Garamond:wght@400&display=swap">
<style>
  :root {
    --page: #f4f4f3;
    --board: #ffffff;
    --ink: #1a1a1a;
    --fold: #d6d6d6;
    --edge: #c9c9c9;
  }
  * { box-sizing: border-box; margin: 0; padding: 0; }
  html, body { width: 1200px; height: 800px; overflow: hidden; background: var(--page); }
  body { font-family: "EB Garamond", serif; color: var(--ink); }

  .dieline {
    position: absolute; left: 120px; top: 28px;
    width: 960px; height: 744px;
    background: var(--board);
    border: 1px solid var(--edge);
    box-shadow: 0 2px 6px rgba(0,0,0,0.12);
    display: flex;
  }
  .panel {
    position: relative; width: 240px; height: 100%;
    border-right: 1px solid var(--fold);
    text-align: center;
  }
  .panel:last-child { border-right: none; }
  .block { position: absolute; left: 0; right: 0; }

  .framed {
    border: 1px solid var(--ink);
    margin: 0 12px;
    padding: 6px 6px 8px;
    font-size: 14.5px; line-height: 19px;
  }
  .framed-title {
    display: block; font-size: 14px; letter-spacing: 0.06em;
    margin-top: -16px; background: var(--board); width: max-content;
    margin-left: auto; margin-right: auto; padding: 0 4px;
  }

  .caution { font-size: 12.5px; line-height: 15px; padding: 0 14px; }
  .caution-title { font-size: 13px; letter-spacing: 0.05em; display: block; }

  .brand-mark {
    display: flex; flex-direction: column; align-items: center;
  }
  .brand-name {
    font-family: "Cormorant Garamond", serif; font-weight: 400;
    letter-spacing: 0.14em; line-height: 1;
  }
  .brand-name.large { font-size: 44px; }
  .brand-name.medium { font-size: 38px; }
  .brand-rule { width: 172px; height: 1px; background: var(--ink); }

  .product-title { font-size: 21px; font-weight: 600; line-height: 1.1; }
  .product-title.ruled { display: inline-block; border-bottom: 1px solid var(--ink); padding: 0 4px 3px; }

  .body-copy { font-size: 15px; line-height: 19px; padding: 0 22px; }
  .body-copy p + p { margin-top: 14px; }
  .body-copy strong { font-weight: 600; }

  .volume { font-size: 15.5px; font-weight: 600; }
  .origin { font-size: 15.5px; }

  .directions h3 { font-size: 15px; font-weight: 600; margin-top: 8px; }
  .directions h3:first-of-type { margin-top: 0; }

  .visit { font-size: 13px; line-height: 16px; }
  .visit .url { font-weight: 600; }
  .handle { display: inline-flex; align-items: center; gap: 4px; font-weight: 600; }

  .care-icons { display: flex; justify-content: center; gap: 10px; }
</style>
</head>
<body>
  <main class="dieline" aria-label="Dusk Haven essential oil box, flat layout">

    <!-- Panel: ingredients and caution -->
    <section class="panel panel-ingredients">
      <div class="block" style="top:155px;">
        <div class="framed">
          <span class="framed-title">INGREDIENTS:</span>
          Lavandula Angustifolia (Australian Lavender), Vetiveria Zizanoides (Vetiver) Root Oil, Sweet Vanilla Fragrant Oil, Pelargonium Capitatum (Cape Rose Geranium) Leaf Extract, Juniperus Virginiana (Cedarwood) Wood Oil, Citrus Limon (Australian Lemon) Peel Oil, Origanum Majorana (Marjoram) Leaf Oil, Cananga Odorata (Ylang Ylang) Flower Oil, Anthemis Nobilis (Roman Chamomile) Flower Oil
        </div>
      </div>
      <div class="block caution" style="top:622px;">
        <span class="caution-title">CAUTION:</span>
        Possible skin sensitivity. Keep out of reach of children. Not for ingestion or internal use. Avoid contact with eyes, inner ears and sensitive areas.
      </div>
    </section>

    <!-- Panel: front face -->
    <section class="panel panel-front">
      <div class="block brand-mark" style="top:196px;">
        <svg width="58" height="58" viewBox="0 0 58 58" aria-hidden="true">
          <circle cx="29" cy="29" r="26" fill="none" stroke="var(--ink)" stroke-width="2"/>
        </svg>
        <div class="brand-name medium" style="margin-top:62px;">DUSK<br>HAVEN</div>
      </div>
      <div class="block" style="top:508px;">
        <span class="product-title ruled">Essential Oil Blend</span>
      </div>
      <div class="block body-copy" style="top:552px; padding:0 18px;">
        Essential Oils have been used for centuries to help prepare the mind and body for sleep.
      </div>
      <div class="block origin" style="top:680px;">Made in Australia</div>
      <div class="block volume" style="top:706px;">1/2 fl.oz./15 mL</div>
    </section>

    <!-- Panel: directions -->
    <section class="panel panel-directions">
      <div class="block" style="top:152px;">
        <div class="framed directions">
          <span class="framed-title">DIRECTIONS:</span>
          <h3>Diffuse</h3>
          <p>Add 4-6 drops to a diffuser or oil burner at night to create a calm and grounded environment.</p>
          <h3>Bathe</h3>
          <p>Add 2-4 drops to a warm bath to help calm the body and mind.</p>
          <h3>Inhale</h3>
          <p>Place 2 drops in the palms of the hands and inhale directly to ease you into a restful sleep.</p>
          <h3>Massage</h3>
          <p>Dilute 4 drops with a carrier oil (such as jojoba or coconut), and massage into the feet before sleep.</p>
        </div>
      </div>
      <div class="block visit" style="top:680px;">
        Visit<br>
        <span class="url">www.duskhaven.com.au</span><br>
        <span class="handle">
          <svg width="11" height="11" viewBox="0 0 11 11" aria-hidden="true"><circle cx="5.5" cy="5.5" r="5" fill="var(--ink)"/></svg>
          @duskhavenau
        </span><br>
        to learn more
      </div>
    </section>

    <!-- Panel: brand side -->
    <section class="panel panel-brand">
      <div class="block brand-mark" style="top:42px;">
        <div class="brand-name medium">DUSK<br>HAVEN</div>
        <div class="brand-rule" style="margin-top:8px;"></div>
      </div>
      <div class="block" style="top:142px;">
        <span class="product-title">Essential Oil Blend</span>
      </div>
      <div class="block body-copy" style="top:272px;">
        <p>Dusk Haven contain a balanced blend of the most sleep supporting essential oils, renowned for their grounding and calming properties.</p>
        <p><strong>Lavender</strong> for restfulness<br>
        <strong>Vetiver</strong> for grounding<br>
        <strong>Cedarwood</strong> for relaxation<br>
        <strong>Marjoram</strong> for balance<br>
        <strong>Roman Chamomile</strong> for comfort</p>
        <p>Add Dusk Haven to your nightly bedtime ritual to help support you in achieving deep and rejuvenating sleep.</p>
      </div>
      <div class="block care-icons" style="top:668px;">
        <svg width="22" height="20" viewBox="0 0 22 20" aria-label="Recyclable" role="img">
          <path d="M11 2 L19 16 L3 16 Z" fill="none" stroke="var(--ink)" stroke-width="1.3"/>
          <path d="M9 5 L11 2 L13 5" fill="none" stroke="var(--ink)" stroke-width="1.3"/>
        </svg>
        <svg width="22" height="20" viewBox="0 0 22 20" aria-label="12 months after opening" role="img">
          <rect x="4" y="2" width="14" height="3" fill="none" stroke="var(--ink)" stroke-width="1.2"/>
          <rect x="3" y="6" width="16" height="12" rx="1" fill="none" stroke="var(--ink)" stroke-width="1.2"/>
          <text x="11" y="15.5" font-size="7" font-family="sans-serif" font-weight="700" text-anchor="middle" fill="var(--ink)">12M</text>
        </svg>
      </div>
      <div class="block volume" style="top:706px;">1/2 fl.oz./15 mL</div>
    </section>

  </main>
</body>
</html>
```